UK Finance Lead Generation Website Design

We need a new design, logo and coding for our website PickBrightRates.com.

Our site uses Pay Per Click traffic in order to generate Life Insurance, Private Medical Insurance, Mortgage & Income Protection leads for BRX regulated brokers from the UK.

So we are looking for a homepage design, landing page/quote page design, thank-you page/privacy/t&c/faq page designs (these will all look very similar as they are just blocks of text).

We are open to all kinds of homepage designs. A good example of a homepage we like is - http://www.ratebazaarhub.com. It essentially is a header, CTAs leading to quoting pages for different products, some text block space and footer.

We however have strict requirements for the landing page/quoting pages for the products. Attached are two wireframes for the Life Insurance Landing Page/Quoting page. The most important thing about the landing page design is for it to be a 2 step process. User completes some dropdown and/or radio buttons on step 1, clicks next step and the form changes a longer one asking for personal details (name, email, phone, address etc) with text on the left saying "Congratulations, we've found few quotes for you, just complete our form etc."
The site that we've got that idea from is here - http://www.cover-plan-guide.co.uk/norvale/. Please have in mind we don't like their design, it is just the layout that inspired us.
Here is also a link to our current Life Insurance Landing Page/Quote Page - http://pickbrightrates.com/life-insurance/norvale.php. It also uses 2 step process however it looks ugly, cluttered and does not convert good for us. From our current landing page you can get the fields the form should ask on step 1 and on step 2.

Any color scheme can be used.

For text/copy please use text from http://www.cover-plan-guide.co.uk/norvale/.

An overview of what we need from this project:
- Logo - the name in the logo should be PickBrightRates
- Homepage design
- Landing page/quoting page design - focus on designing a good Life Insurance Landing Page/Quoting page and with slight variations this page will be adjusted for Private Medical Insurance, Income Protection & Mortgages
- About us/Privacy/T&C/FAQs/Thank-you page design - one design/layout will satisfy all that is needed for these pages.
- Coding of everything (HTML, CSS, JAVASCRIPT) + form validation (we will provide the syntax/rules for the form validation) + tooltips on form fields (as in the provided example http://www.cover-plan-guide.co.uk/norvale/)

What is most important for us:
- Getting a landing page/quoting page design that converts!

Target Market(s)

18-60 UK Males & Females looking for financial quotes

Logo Text

PickBrightRates

Coding

Number of Pages Required

5+ page

Requirements
Must have
• 2 Step form for Landing Page/Quoting Page
Nice to have
• Modern & clean design.
• Responsive layout/mobile layout

```html
<!DOCTYPE html>
<html lang="en">
<head>
<meta charset="utf-8">
<title>PickBrightRates – Life Insurance Quotes</title>
<link href="https://fonts.googleapis.com/css2?family=Open+Sans:wght@400;600;700&display=swap" rel="stylesheet">
<style>
:root{
  --green:#2e9a3e;--green-dark:#1f6e2c;--green-deep:#135c25;--green-light:#6cc04a;
  --orange:#f47b16;--red:#e8261b;--red-dark:#b9170f;
  --ink:#222;--muted:#555;--line:#ccc;--paper:#fff;--soft:#f2f2f2;
}
*{box-sizing:border-box;margin:0;padding:0}
html,body{width:761px;height:1200px;overflow:hidden}
body{position:relative;font-family:"Open Sans",Arial,sans-serif;color:var(--ink);background:var(--paper)}
a{text-decoration:none}
.abs{position:absolute}
.hero-bg{left:0;top:0;width:761px;height:437px;background:linear-gradient(100deg,#262d35 0%,#3a434d 45%,#2a3139 70%,#5a5f66 100%)}
.header{left:38px;top:20px;width:685px;height:96px;background:var(--paper)}
.brand{left:12px;top:14px;display:flex;align-items:center;gap:7px;font-weight:700;font-size:17px;color:var(--ink);letter-spacing:.2px}
.brand-mark{width:24px;height:24px;background:var(--green)}
.contact{right:48px;top:12px;text-align:right}
.contact .phone{font-size:15px}
.contact .hours{font-size:8px;margin-top:3px}
.chat{right:13px;top:20px;font-size:8px;color:var(--green);font-weight:600}
.nav{left:9px;top:61px;width:667px;height:25px;display:flex;background:var(--green)}
.nav a{flex:auto;display:flex;align-items:center;justify-content:center;color:#fff;font-size:8px;border-right:1px solid var(--green-dark)}
.nav a:last-child{border:0}
.nav a.active{background:var(--green-light)}
.arrow-btn{top:233px;width:24px;height:24px;border:2px solid #777;border-radius:50%}
.hero-panel{left:74px;top:154px;width:604px;height:246px;background:#000}
.hero-title{left:25px;top:22px;color:#fff;font-size:20px;font-weight:400;white-space:nowrap}
.hero-title b{font-weight:600}
.insurer{left:60px;top:84px;width:150px;display:flex;align-items:center;justify-content:center;gap:7px;color:#fff;font-weight:400;font-size:17px}
.insurer i{width:12px;height:12px;border-radius:50%;background:#fff}
.perks{left:26px;top:134px;list-style:none;color:#fff;font-size:12px;line-height:17.5px}
.perks li{display:flex;align-items:center;gap:15px}
.perks li::before{content:"✓";width:9px;height:9px;border-radius:50%;background:#fff;color:#000;font-size:7px;display:flex;align-items:center;justify-content:center;font-weight:700}
.quote{left:328px;top:162px;width:342px;height:231px;background:var(--paper)}
.quote-head{height:33px;background:var(--orange);color:#fff;font-size:17px;font-weight:600;display:flex;align-items:center;justify-content:center}
.field{left:35px;display:flex;align-items:center;font-size:9.5px;color:var(--muted)}
.field .q{width:8px;height:8px;border-radius:50%;background:var(--red);margin-right:5px;color:#fff;font-size:6px;display:flex;align-items:center;justify-content:center}
.select{left:142px;width:166px;height:22px;border:1px solid #ddd;background:var(--paper)}
.select span{position:absolute;right:0;top:0;width:20px;height:20px;background:#ccc}
.select.on span{background:var(--green)}
.radio{width:10px;height:10px;border:1px solid #999;border-radius:50%;display:inline-block;vertical-align:middle;margin-right:8px}
.radio.on{box-shadow:inset 0 0 0 2px #fff;background:var(--green)}
.seal{left:36px;top:174px;width:64px;height:28px;border-radius:14px;background:#ddd}
.cta-quote{left:166px;top:168px;width:146px;height:32px;background:var(--red);color:#fff;font-size:14px;display:flex;align-items:center;justify-content:center}
.safe{left:166px;top:207px;width:146px;text-align:center;font-size:7.5px;color:var(--muted)}
.close{left:668px;top:148px;width:14px;height:14px;border-radius:50%;background:#000;border:1px solid #fff;color:#fff;font-size:8px;display:flex;align-items:center;justify-content:center}
.partners{left:0;top:437px;width:761px;height:55px;background:var(--soft);display:flex;justify-content:center;align-items:center;gap:18px;font-size:8.5px;font-weight:600;color:#1d4f8f}
.h2{width:761px;text-align:center;font-size:14px;font-weight:400}
.step{top:562px;width:207px;height:72px;border:1px solid var(--line);background:var(--paper)}
.step-icon{left:4px;top:4px;width:63px;height:62px;background:var(--green-dark);color:#fff;font-size:10px;display:flex;flex-direction:column;align-items:center;justify-content:center;gap:3px}
.step-num{left:50px;top:7px;width:13px;height:13px;background:var(--green-deep);color:#fff;border:1px solid #fff;font-size:8px;display:flex;align-items:center;justify-content:center}
.step-text{left:82px;top:18px;font-size:12.5px;line-height:17px;color:#333;white-space:nowrap}
.welcome-sub{top:697px;width:761px;text-align:center;font-size:10px;color:#333}
.welcome-body{left:46px;top:718px;width:669px;text-align:center;font-size:7.8px;line-height:10.8px;color:var(--muted)}
.section-title{left:38px;top:815px;font-size:14px;font-weight:400}
.carousel-arrows{left:692px;top:817px;display:flex;gap:2px}
.carousel-arrows i{width:13px;height:13px;border:1px solid #555;border-radius:50%;font-style:normal;font-size:8px;line-height:11px;text-align:center;color:#555}
.carousel-arrows i+i{border-color:var(--green);color:var(--green)}
.review{top:854px;width:220px}
.avatar{left:2px;top:0;width:63px;height:63px;border-radius:50%;background:radial-gradient(circle at 50% 40%,#b58a6a,#3a3e44)}
.review h3{position:absolute;left:77px;top:3px;font-size:10px;font-weight:400}
.review p{position:absolute;left:77px;top:20px;width:140px;font-size:7px;line-height:10px}
.review a{position:absolute;left:164px;top:58px;font-size:7px;color:var(--ink)}
.dots{left:368px;top:949px;display:flex;gap:6px}
.dots i{width:4px;height:4px;border-radius:50%;background:#bbb}
.dots i:first-child{background:var(--green)}
.big-cta{left:244px;top:1005px;width:266px;height:36px;background:var(--red);color:#fff;font-size:15px;display:flex;align-items:center;padding-left:16px}
.big-cta span{position:absolute;right:0;top:0;width:42px;height:36px;background:var(--red-dark);display:flex;align-items:center;justify-content:center;font-size:14px}
.footer{left:0;top:1073px;width:761px;height:87px;background:var(--soft);text-align:center}
.footer nav{padding-top:31px;font-size:8px;color:#333}
.footer nav a{color:#333;margin:0 6px}
.footer p{font-size:8px;margin-top:7px}
.bar{left:0;top:1160px;width:761px;height:40px;background:var(--green);color:#fff;font-size:7.5px;padding:15px 37px}
.social{right:40px;top:1173px;display:flex;gap:10px;color:#fff;font-size:7.5px;font-weight:600}
</style>
</head>
<body>
<div class="abs hero-bg" role="img" aria-label="Dark background photo of hands sheltering a small house"></div>

<header class="abs header">
  <div class="abs brand"><i class="brand-mark"></i>PickBrightRates</div>
  <div class="abs contact"><div class="phone">0800 555 0192</div><div class="hours">MON-THURS 9:30AM-8PM | FRI 9:30AM-6PM</div></div>
  <div class="abs chat">Chatly</div>
  <nav class="abs nav">
    <a href="#">HOME</a><a class="active" href="#">FREE QUOTE</a><a href="#">ABOUT US</a><a href="#">CRITICAL ILLNESS</a><a href="#">OVER 50'S</a><a href="#">MORTGAGE PROTECTIONS</a><a href="#">NEWS</a>
  </nav>
</header>

<svg class="abs arrow-btn" style="left:10px" viewBox="0 0 24 24"><path d="M15 12H8M11 8l-4 4 4 4" stroke="#888" stroke-width="2" fill="none"/></svg>
<svg class="abs arrow-btn" style="left:728px" viewBox="0 0 24 24"><path d="M9 12h7M13 8l4 4-4 4" stroke="#888" stroke-width="2" fill="none"/></svg>

<section class="abs hero-panel">
  <h1 class="abs hero-title"><b>Norvale</b> Life Insurance</h1>
  <div class="abs insurer"><i></i>Norvale</div>
  <ul class="abs perks">
    <li>Lorem ipsum dolor sit amet,</li>
    <li>consectetur adipiscing elit.</li>
    <li>Praesent at tristique ex.</li>
    <li>Nam enim nunc, luctus sit amet</li>
    <li>Dignissim eu</li>
  </ul>
</section>

<form class="abs quote">
  <div class="quote-head">Get Free Quote</div>
  <div class="abs field" style="top:49px"><i class="q">?</i>Type of insurance</div>
  <div class="abs select on" style="top:44px"><span></span></div>
  <div class="abs field" style="top:79px"><i class="q">?</i>Cover Period</div>
  <div class="abs select" style="top:74px"><span></span></div>
  <div class="abs field" style="top:109px"><i class="q">?</i>Amount of Cover</div>
  <div class="abs select" style="top:104px"><span></span></div>
  <div class="abs field" style="top:144px">Cover required for</div>
  <div class="abs field" style="left:144px;top:141px;font-size:8px"><i class="radio on"></i>You</div>
  <div class="abs field" style="left:191px;top:141px;font-size:8px"><i class="radio"></i>You &amp; Your Partner</div>
  <div class="abs seal"></div>
  <div class="abs cta-quote">GET A QUOTE</div>
  <div class="abs safe">Safe &nbsp;|&nbsp; Secure &nbsp;|&nbsp; Privacy Protected</div>
</form>
<div class="abs close">✕</div>

<div class="abs partners">
  <span>Norvale</span><span>Medora</span><span>Kestrel</span><span>Orbis</span><span>Silverline</span><span>Fellows Trust</span><span>Harbour &amp; Hale</span><span>Mersey Mutual</span><span>Prospera</span><span>Alpina</span>
</div>

<h2 class="abs h2" style="top:521px">HOW IT WORKS</h2>
<div class="abs step" style="left:38px"><div class="abs step-icon">✓<span>Apply</span></div><div class="abs step-num">1</div><div class="abs step-text">Fill in our form or<br><b style="font-weight:600">Call 0800 555 0192</b></div></div>
<div class="abs step" style="left:277px"><div class="abs step-icon">⇄<span>Compare</span></div><div class="abs step-num">2</div><div class="abs step-text">We compare 100s of<br>life insurance plans</div></div>
<div class="abs step" style="left:517px"><div class="abs step-icon">≡<span>Save</span></div><div class="abs step-num">3</div><div class="abs step-text">You get a free quote<br><b style="font-weight:600">saving up to 45%</b></div></div>

<h2 class="abs h2" style="top:673px">WELCOME TO OUR SITE</h2>
<div class="abs welcome-sub">Find a Great Quote Today!</div>
<p class="abs welcome-body">Our TYPICAL APR is 13.8% (variable). This means two out of three customers receive this or better.Unsecured loans are available from £1,000 to £25,000. Representative 12.6% APR variable. Representative Example: If you borrow £11,000 over 6 years at an annual rate of 8.9% (variable) you will repay £230.63 per month &amp; total amount payable £16,605.36. A broker fee of up to 12.5% will be added to secured loans. Loans may be secured on your home. Think carefully before securing other debts against your home. Your home may be repossessed if you do not keep up repayment on a mortgage or any other debts secured on it. If you are thinking of consolidating existing borrowing you should be aware that you may be extending the terms of the debt and increasing the total amount you repay.</p>

<h2 class="abs section-title">CLIENT TESTIMONIALS</h2>
<div class="abs carousel-arrows"><i>‹</i><i>›</i></div>
<article class="abs review" style="left:38px"><div class="abs avatar" role="img" aria-label="Customer portrait photo"></div><h3>JHON DOE</h3><p>Donec sed lorem tincidunt, viverra diam vel, auctor dolor. Donec urna magna, auctor porttitor</p><a href="#">Read More ➔</a></article>
<article class="abs review" style="left:273px"><div class="abs avatar" role="img" aria-label="Customer portrait photo"></div><h3>JHON DOE</h3><p>Donec sed lorem tincidunt, viverra diam vel, auctor dolor. Donec urna magna, auctor porttitor</p><a href="#">Read More ➔</a></article>
<article class="abs review" style="left:505px"><div class="abs avatar" role="img" aria-label="Customer portrait photo"></div><h3>JHON DOE</h3><p>Donec sed lorem tincidunt, viverra diam vel, auctor dolor. Donec urna magna, auctor porttitor</p><a href="#">Read More ➔</a></article>
<div class="abs dots"><i></i><i></i><i></i><i></i></div>

<a class="abs big-cta" href="#">GET A FREE QUOTE NOW<span>➡</span></a>

<footer class="abs footer">
  <nav><a href="#">Home</a>|<a href="#">About Us</a>|<a href="#">Blog</a>|<a href="#">Why Choose Us?</a>|<a href="#">FAQs</a>|<a href="#">Contact Us</a>|<a href="#">Sitemap</a>|<a href="#">Privacy Policy</a>|<a href="#">Terms &amp; Conditions</a></nav>
  <p>2015 Pick Bright Rates. ALL RIGHTS RESERVED. BRIGHTLEAD LTD - 14 ALDER COURT, LEEDS, LS2 9ZZ.</p>
</footer>
<div class="abs bar">© 2015 yoursite. All rights reserved.</div>
<div class="abs social"><span>Loop</span><span>Chirp</span><span>Pix</span></div>
</body>
</html>
```